Website for enterprise software start-up

We need a new Wordpress website. We are an early stage start-up focused on mobile video technology for cellular operators. The audience is strategy, marketing and customer acquisition execs from the operators.

The purpose of the site is to act as a sales brochure and capture leads. A demo app can be downloaded from the current site, want to put that behind a contact form.

Current website is at www.brellowmo.tv. Similar number of pages. Looking for a clean design template, with minimal customization. Blog will remain as is.

Want to be able to modify the copy via Wordpress. Reference designs I like: vandrisk.com, tallowquarrymetric.com

Target Market(s)

Mobile operators and MVNOs in the US and Asia Pacific regions

Industry/Entity Type

Business Software

Coding

Coded - Design and coding required

Number of Pages Required

4 page

Font styles to use
Sans Serif

Colors
f78f20

Requirements
Must have
• Form for downloading sample apps.
• Landing page with image, Product, Blog, About, Contact
• Team page

```html
<!DOCTYPE html>
<html lang="en">
<head>
<meta charset="utf-8">
<title>brellowmo — Home</title>
<link rel="stylesheet" href="https://fonts.googleapis.com/css2?family=Open+Sans:ital,wght@0,300;0,400;0,600;0,700;1,400&display=swap">
<style>
:root{
  --orange:#f78f20;
  --orange-soft:rgba(247,143,32,.86);
  --ink:#2f3336;
  --text:#6d7377;
  --muted:#9aa0a4;
  --rule:#dfe2e5;
  --panel:#eceef0;
  --band:#e4e6e8;
  --white:#ffffff;
}
*{box-sizing:border-box;margin:0;padding:0}
html,body{width:863px;height:1200px;overflow:hidden;background:var(--white)}
body{font-family:"Open Sans",Arial,sans-serif;color:var(--text);font-size:8px;line-height:1.5}
.page{position:relative;width:863px;height:1200px;overflow:hidden}

/* header */
.site-header{position:absolute;left:0;top:0;width:863px;height:86px;border-top:3px solid var(--ink)}
.brand{position:absolute;left:28px;top:20px;display:flex;align-items:center;gap:10px}
.brand-mark{width:40px;height:40px;background:var(--orange)}
.brand-name{font-size:32px;font-weight:700;color:var(--ink);letter-spacing:-.5px}
.main-nav{position:absolute;left:345px;top:34px;display:flex;gap:26px}
.main-nav a{font-size:8px;font-weight:600;text-transform:uppercase;color:var(--ink);text-decoration:none;letter-spacing:.5px;padding-bottom:6px}
.main-nav a.active{color:var(--orange);border-bottom:2px solid var(--orange)}

.breadcrumb{position:absolute;left:0;top:86px;width:863px;height:20px;background:var(--orange)}
.breadcrumb span{position:absolute;left:345px;top:4px;color:var(--white);font-size:8px;font-weight:600}

/* hero */
.hero{position:absolute;left:0;top:106px;width:863px;height:256px}
.hero-photo{position:absolute;inset:0;background:linear-gradient(90deg,#c9d6df 0%,#8aa6bc 30%,#d0a172 48%,#e89a4a 58%,#5d87a8 72%,#2c4e6c 100%)}
.hero-sea{position:absolute;left:0;bottom:0;width:360px;height:90px;background:linear-gradient(180deg,#4d6d86,#1f3549)}
.hero-caption{position:absolute;left:290px;top:140px;width:490px;height:100px;background:var(--orange-soft);display:flex}
.hero-title{width:170px;padding:12px 0 0 30px;color:var(--white)}
.hero-title h1{font-size:40px;font-weight:600;line-height:1}
.hero-title p{font-size:7px;margin-top:6px}
.hero-text{flex:1;padding:14px 24px 0 0;color:var(--white);font-size:7.5px}
.hero-text .date{margin-top:8px;font-weight:600}

/* sections */
.sidebar-block{position:absolute;left:0;width:275px;padding:0 24px}
.sidebar-block h2{font-size:12px;font-weight:400;color:var(--orange);text-transform:uppercase;padding-bottom:8px;border-bottom:1px solid var(--rule);margin-bottom:6px}
.side-list{list-style:none}
.side-list li{font-size:8px;padding:6px 0 6px 14px;border-bottom:1px solid var(--rule);position:relative}
.side-list li::before{content:"›";position:absolute;left:2px;top:4px;color:var(--orange);font-size:11px;line-height:1}
.more{display:inline-block;color:var(--orange);font-size:8px;margin-top:6px;text-decoration:none}

.services-panel{position:absolute;left:275px;top:400px;width:588px;height:200px;background:var(--panel);display:flex;padding:26px 14px 0 16px;gap:18px}
.service{flex:1}
.service h3{font-size:18px;font-weight:300;color:var(--ink);text-transform:uppercase}
.service h3 em{font-style:italic;color:var(--orange)}
.service h4{font-size:9px;font-weight:700;color:var(--ink);margin:6px 0}
.service p{font-size:7.5px}

.projects-media{position:absolute;left:275px;top:620px;width:588px;height:270px;display:flex}
.project-feature{position:relative;width:294px;height:270px;background:linear-gradient(160deg,#f6a24a,#e07d1c 60%,#b8621a)}
.project-feature .overlay{position:absolute;left:18px;top:22px;right:18px;color:var(--white)}
.project-feature h3{font-size:11px;font-weight:600;margin-bottom:6px}
.project-feature p{font-size:7.5px}
.project-photo{width:294px;height:270px;background:linear-gradient(200deg,#dfe9f1,#7f9fbc 45%,#2e4e6d)}

.profile{position:absolute;left:290px;top:918px;width:555px}
.profile h2{font-size:38px;font-weight:600;color:var(--orange);line-height:1.1;margin-bottom:8px}
.profile .lead{font-size:8.5px;font-weight:700;color:var(--ink);margin-bottom:8px}
.profile p{font-size:7.5px;margin-bottom:8px}

.clients-band{position:absolute;left:275px;top:1070px;width:588px;height:130px;background:var(--band);display:flex;align-items:center;justify-content:space-around}
.client{display:flex;align-items:center;gap:8px;font-size:13px;font-weight:600;color:#7b8186}
.client-dot{width:34px;height:34px;border-radius:50%;border:2px solid #9ca2a6}
</style>
</head>
<body>
<div class="page">

  <header class="site-header">
    <div class="brand"><div class="brand-mark"></div><span class="brand-name">brellowmo</span></div>
    <nav class="main-nav">
      <a class="active" href="#">Home</a><a href="#">About</a><a href="#">Gallery</a><a href="#">Pages</a><a href="#">Contact</a>
    </nav>
  </header>
  <div class="breadcrumb"><span>Home</span></div>

  <section class="hero">
    <div class="hero-photo" role="img" aria-label="Photo of a boat on a calm sea beside a modern glass office tower"></div>
    <div class="hero-sea" role="img" aria-label="Sea and coastline"></div>
    <div class="hero-caption">
      <div class="hero-title"><h1>Guest</h1><p>Lorem ipsum dolor sit amet</p></div>
      <div class="hero-text">
        <p>Lorem ipsum dolor sit amet, consectetur adipiscing elit. Suspendisse tristique ante sit amet sem pulvinar posuere felis varius.</p>
        <p class="date">Oct 04 — Dec 12 2014</p>
      </div>
    </div>
  </section>

  <aside class="sidebar-block" style="top:428px">
    <h2>Services</h2>
    <ul class="side-list">
      <li>Lorem ipsum dolor sit amet</li>
      <li>Consectetur adipiscing elit</li>
      <li>Suspendisse tristique ante</li>
      <li>Donec pulvinar posuere</li>
    </ul>
  </aside>

  <section class="services-panel">
    <article class="service">
      <h3>Web <em>.01</em></h3>
      <h4>Pellentesque habitant morbi tristique</h4>
      <p>Lorem ipsum dolor sit amet, consectetur adipiscing elit. Suspendisse tristique ante sit amet sem.</p>
      <a class="more" href="#">view more</a>
    </article>
    <article class="service">
      <h3>Motion <em>.02</em></h3>
      <h4>Pellentesque habitant morbi tristique</h4>
      <p>Lorem ipsum dolor sit amet, consectetur adipiscing elit. Suspendisse tristique ante sit amet sem.</p>
      <a class="more" href="#">view more</a>
    </article>
    <article class="service">
      <h3>Print <em>.03</em></h3>
      <h4>Pellentesque habitant morbi tristique</h4>
      <p>Lorem ipsum dolor sit amet, consectetur adipiscing elit. Suspendisse tristique ante sit amet sem.</p>
      <a class="more" href="#">view more</a>
    </article>
  </section>

  <aside class="sidebar-block" style="top:648px">
    <h2>Projects</h2>
    <a class="more" href="#">[more]</a>
  </aside>

  <section class="projects-media">
    <div class="project-feature" role="img" aria-label="Warm orange-toned project photograph">
      <div class="overlay">
        <h3>Lorem ipsum dolor sit amet consectetur</h3>
        <p>Suspendisse tristique ante sit amet sem pulvinar posuere. Pellentesque habitant morbi tristique senectus et netus et malesuada fames.</p>
      </div>
    </div>
    <div class="project-photo" role="img" aria-label="Glass office building against a blue sky"></div>
  </section>

  <aside class="sidebar-block" style="top:912px">
    <h2>About Us</h2>
    <ul class="side-list">
      <li>Lorem ipsum dolor sit amet</li>
      <li>Consectetur adipiscing elit</li>
      <li>Suspendisse tristique ante</li>
      <li>Donec pulvinar posuere</li>
    </ul>
  </aside>

  <section class="profile">
    <h2>Profile</h2>
    <p class="lead">Lorem ipsum dolor sit amet, consectetur adipiscing elit. Suspendisse tristique ante sit amet sem pulvinar posuere. Pellentesque habitant morbi tristique senectus et netus et malesuada fames ac turpis egestas.</p>
    <p>Suspendisse rhoncus facilisis adipiscing. Vestibulum ante ipsum primis in faucibus orci luctus et ultrices posuere cubilia curae. Donec vitae nisl et augue fermentum dignissim. Sed tempus felis vel nibh dapibus vitae luctus quam aliquam, nunc at bibendum tristique, ipsum lorem commodo neque, non varius elit lorem ut massa.</p>
    <p>Aenean vehicula augue eget nunc cursus sed mattis nisl posuere. Fusce eget velit id magna fermentum congue. Nam consequat, libero vel tincidunt rutrum, risus lorem dapibus erat, sed aliquam metus sapien non lectus. Integer at orci vitae arcu tempus elementum.</p>
    <a class="more" href="#">view all</a>
  </section>

  <aside class="sidebar-block" style="top:1092px">
    <h2>Our Clients</h2>
    <a class="more" href="#">[more]</a>
  </aside>

  <section class="clients-band">
    <div class="client">Mossgrave</div>
    <div class="client"><span class="client-dot"></span>Corvel</div>
    <div class="client">Penwick</div>
    <div class="client"><span class="client-dot"></span>Aldermoor</div>
  </section>

</div>
</body>
</html>
```